Brennick Drilling Inc. Business card design

Business card design for "Brennick Drilling Inc. - Directional Drilling Services"

Address is:

Brennick Drilling Inc.
512 - 73 Tarvel Crescent SW
Calgary, Alberta, Canada
T2K 4P8

Please incorporate the logo design into the card, thank you.

Target Market(s)

Oil & Gas and Drilling

Industry/Entity Type

Business

```html
<!DOCTYPE html>
<html lang="en">
<head>
<meta charset="utf-8">
<title>Brennick Drilling Inc. – Business Card</title>
<link href="https://fonts.googleapis.com/css2?family=Open+Sans:wght@400;600;700&family=Exo+2:wght@500&display=swap" rel="stylesheet">
<style>
  :root {
    --backdrop: #2a2624;
    --card: #0d0d0d;
    --card-edge: #1a1a1a;
    --emboss: #262626;
    --red: #e0262d;
    --white: #f4f4f4;
    --grey: #bdbdbd;
  }
  * { box-sizing: border-box; margin: 0; padding: 0; }
  html, body { width: 1200px; height: 716px; overflow: hidden; }
  body {
    background: var(--backdrop);
    font-family: "Open Sans", Arial, sans-serif;
    position: relative;
  }
  .card {
    position: absolute;
    top: 215px;
    width: 500px;
    height: 286px;
    background: var(--card);
    border: 1px solid var(--card-edge);
    border-radius: 4px;
    box-shadow: 0 12px 30px rgba(0,0,0,.45);
    overflow: hidden;
  }
  .card--back { left: 70px; }
  .card--front { left: 630px; }

  /* back */
  .back-brand {
    position: absolute; inset: 0;
    display: flex; flex-direction: column; align-items: center; justify-content: center; gap: 14px;
  }
  .back-brand__mark {
    width: 70px; height: 70px; border-radius: 50%;
    border: 3px solid var(--emboss);
  }
  .back-brand__name {
    font-weight: 700; font-size: 26px; letter-spacing: 1px;
    color: var(--emboss); text-transform: uppercase;
  }

  /* front */
  .front-brand {
    position: absolute; top: 26px; left: 0; right: 0;
    display: flex; flex-direction: column; align-items: center; gap: 8px;
  }
  .front-brand__mark {
    width: 42px; height: 42px; border-radius: 50%;
    border: 3px solid var(--white);
  }
  .front-brand__name {
    font-weight: 700; font-size: 17px; letter-spacing: .5px;
    color: var(--white); text-transform: uppercase;
  }
  .rule {
    position: absolute; height: 2px; background: var(--red);
  }
  .rule--left { left: 0; top: 108px; width: 120px; }
  .rule--right { right: 0; top: 128px; width: 120px; }
  .holder {
    position: absolute; top: 112px; left: 0; right: 0; text-align: center;
  }
  .holder__name {
    font-family: "Exo 2", "Open Sans", sans-serif;
    font-weight: 500; font-size: 22px; letter-spacing: 1.5px;
    color: var(--red); text-transform: uppercase;
  }
  .holder__role {
    font-weight: 600; font-size: 10px; letter-spacing: .5px; color: var(--white);
  }
  .details {
    position: absolute; top: 178px; left: 0; right: 0;
    display: flex; justify-content: center;
  }
  .contacts {
    list-style: none; padding-right: 16px; border-right: 2px solid var(--red);
    display: flex; flex-direction: column; gap: 6px; align-items: flex-end;
  }
  .contacts li {
    display: flex; align-items: center; gap: 7px;
    font-size: 10.5px; color: var(--white);
  }
  .contacts svg { width: 13px; height: 13px; display: block; }
  .address {
    padding-left: 16px; font-style: normal;
    font-size: 11px; line-height: 1.55; color: var(--white);
  }
  .address__company { color: var(--red); font-weight: 700; }
</style>
</head>
<body>

  <section class="card card--back" aria-label="Card back">
    <div class="back-brand">
      <span class="back-brand__mark"></span>
      <span class="back-brand__name">Brennick Drilling Inc.</span>
    </div>
  </section>

  <section class="card card--front" aria-label="Card front">
    <div class="front-brand">
      <span class="front-brand__mark"></span>
      <span class="front-brand__name">Brennick Drilling Inc.</span>
    </div>

    <span class="rule rule--left"></span>
    <span class="rule rule--right"></span>

    <div class="holder">
      <p class="holder__name">Marcus D. Halloway</p>
      <p class="holder__role">MANAGER</p>
    </div>

    <div class="details">
      <ul class="contacts">
        <li>403-555-0187
          <svg viewBox="0 0 13 13"><rect width="13" height="13" rx="2" fill="#e0262d"/><path d="M4 3.2l1.4 0 .6 2-1 .7a5 5 0 0 0 2.1 2.1l.7-1 2 .6 0 1.4c-3.2.3-6.1-2.6-5.8-5.8z" fill="#fff"/></svg>
        </li>
        <li>marcus10@brennickdrilling.com
          <svg viewBox="0 0 13 13"><rect width="13" height="13" rx="2" fill="#e0262d"/><rect x="3" y="4" width="7" height="5" fill="none" stroke="#fff" stroke-width="1"/><path d="M3 4l3.5 3L10 4" fill="none" stroke="#fff" stroke-width="1"/></svg>
        </li>
        <li>www.brennickdrilling.com
          <svg viewBox="0 0 13 13"><rect width="13" height="13" rx="2" fill="#e0262d"/><circle cx="6.5" cy="6.5" r="3.5" fill="none" stroke="#fff" stroke-width="1"/><path d="M3 6.5h7M6.5 3c-1.5 2-1.5 5 0 7M6.5 3c1.5 2 1.5 5 0 7" fill="none" stroke="#fff" stroke-width=".8"/></svg>
        </li>
      </ul>
      <address class="address">
        <span class="address__company">Brennick Drilling Inc.</span><br>
        512 - 73 Tarvel Crescent SW<br>
        Calgary, Alberta, Canada, T2K 4P8
      </address>
    </div>
  </section>

</body>
</html>
```